New fishing tackle company needs packet design!

We are an innovative new fishing tackle company, producing lifelike soft plastic fishing lures, based in Australia but will hopefully expand worldwide in the years to come. We need a packaging designed for these lures (roughly a rectangle 21cm x 14cm) that is both eye catching and modern, but at the same time not over complicated. I would like the BRAVO Angling Gear logo to be a large feature on the front, possibly in the top left hand quarter of the packet. These lures are biodegradable so I would like to promote that in some form and also have part of the front as a "clear window" to the inside of the packet showing the lures inside. I don't have any specific colour at this point in time.
Updates

Target Market(s)

Men between the ages of 16 and 40

Industry/Entity Type

It Company

Colors

Designer to choose colors to be used in the design.

Requirements
Must have
• Bravo Angling Logo, Clear portion to show product inside.
Nice to have
• Biodegradable logo or reference
Should not have
• Corny fishing logo, cartoons

```html
<!DOCTYPE html>
<html lang="en">
<head>
<meta charset="utf-8">
<title>Bravo Angling – Fishing Lures Packet</title>
<link href="https://fonts.googleapis.com/css2?family=Russo+One&display=swap" rel="stylesheet">
<style>
  :root {
    --window: #eef0f2;
    --brand-blue: #0a4fa6;
    --brand-blue-deep: #06357a;
    --water-blue: #1b9ad6;
    --silver: #d6dbe0;
    --silver-dark: #8d959c;
    --ink: #0c0c0c;
    --paper: #ffffff;
    --badge-green: #a9c43a;
    --badge-blue: #1c7fbf;
  }
  html, body {
    margin: 0;
    padding: 0;
    width: 1200px;
    height: 802px;
    overflow: hidden;
    background: var(--paper);
  }
  .packet {
    position: relative;
    width: 1200px;
    height: 802px;
    overflow: hidden;
    font-family: "Russo One", "Arial Black", sans-serif;
  }
  .packet-art {
    position: absolute;
    inset: 0;
    display: block;
  }
  .brand-name {
    position: absolute;
    left: 30px;
    top: 218px;
    width: 430px;
    margin: 0;
    color: var(--silver);
    font-family: "Russo One", "Arial Black", sans-serif;
    font-weight: 400;
    text-align: center;
    line-height: 1;
  }
  .brand-name .brand-main {
    display: block;
    font-size: 78px;
    letter-spacing: 2px;
  }
  .brand-name .brand-sub {
    display: block;
    margin-top: 14px;
    padding-left: 90px;
    font-size: 22px;
    letter-spacing: 3px;
  }
  .product-title {
    font-family: "Russo One", "Arial Black", sans-serif;
    fill: var(--ink);
    stroke: var(--paper);
    stroke-width: 12px;
    paint-order: stroke fill;
    stroke-linejoin: round;
  }
</style>
</head>
<body>
<main class="packet">
  <svg class="packet-art" viewBox="0 0 1200 802" width="1200" height="802">
    <defs>
      <linearGradient id="brandOval" x1="0" y1="0" x2="0" y2="1">
        <stop offset="0" stop-color="var(--brand-blue)"/>
        <stop offset="1" stop-color="var(--brand-blue-deep)"/>
      </linearGradient>
      <linearGradient id="silverEdge" x1="0" y1="0" x2="1" y2="1">
        <stop offset="0" stop-color="#ffffff"/>
        <stop offset="0.5" stop-color="var(--silver-dark)"/>
        <stop offset="1" stop-color="#f4f6f8"/>
      </linearGradient>
      <linearGradient id="badgeFill" x1="0" y1="0" x2="0" y2="1">
        <stop offset="0" stop-color="var(--badge-green)"/>
        <stop offset="0.55" stop-color="#5fb07a"/>
        <stop offset="1" stop-color="var(--badge-blue)"/>
      </linearGradient>
    </defs>

    <rect class="clear-window" x="0" y="0" width="1200" height="802" fill="var(--window)"
          role="img" aria-label="Clear window showing the lures inside the packet"/>

    <path class="water-band" d="M 95 802 Q 760 560 960 0 L 1200 0 L 1200 285 Q 700 560 190 802 Z"
          fill="var(--water-blue)" role="img" aria-label="Water band with rising bubbles"/>
    <path class="band-edge" d="M 190 802 Q 700 560 1200 285 L 1200 305 Q 710 580 225 802 Z"
          fill="url(#silverEdge)"/>

    <path class="dark-corner" d="M 720 802 Q 1000 640 1200 392 L 1200 802 Z" fill="var(--ink)"/>
    <path class="dark-corner-edge" d="M 700 802 Q 990 630 1200 378 L 1200 392 Q 1000 640 720 802 Z"
          fill="url(#silverEdge)"/>

    <ellipse class="brand-oval-rim" cx="275" cy="165" rx="372" ry="272" transform="rotate(-10 275 165)"
             fill="url(#silverEdge)"/>
    <ellipse class="brand-oval" cx="275" cy="165" rx="358" ry="258" transform="rotate(-10 275 165)"
             fill="url(#brandOval)"/>

    <g transform="rotate(-22 880 300)">
      <text class="product-title" x="870" y="270" text-anchor="middle" font-size="92">FISHING</text>
      <text class="product-title" x="915" y="395" text-anchor="middle" font-size="128">LURES</text>
    </g>

    <circle class="eco-badge" cx="1057" cy="664" r="82" fill="url(#badgeFill)"
            stroke="var(--paper)" stroke-width="6"
            role="img" aria-label="Biodegradable badge"/>
  </svg>

  <h1 class="brand-name">
    <span class="brand-main">BRAVO</span>
    <span class="brand-sub">ANGLING GEAR</span>
  </h1>
</main>
</body>
</html>
```